MYLAR BAG FOR BLOOMA

Ive included a template for the design provided by the printer.

FRONT :
I'd like to match the box , i have a screenshot. I used an app to create it and the box printer somehow applied it. The app tells me the fonts, let me know if you would like the font names.

BACK SIDE :

DIRECTIONS FOR USE : THC TOLERANCE MAY VARY FROM PERSON TO PERSON. THE ACCEPTED RECOMMENDATION FOR A NEW USER IS 10 MG THC. REFERENCE THE AFFIXED TRALVO TAG FOR ACCURATE DOSAGE INFORMATION .

INGREDIENTS : RICE, SUGAR, THC EXTRACT, COCONUT OIL, ARTIFICIAL FLAVOR & COLOR, SALT, MALT SYRUP

ALLERGEN WARNING : CONTAINS COCONUT.
MADE IN A FACULTY THAT HANDLES PEANUTS AND OTHER TREE NUTS.

THE ACTUAL VALUE OF REPORTED CANNABINOIDS MAY VARY FROM THE REPORTED VALUE BY +/-10 %

ACTIVATION TIME :10-60 MIN

WARNING : FOR USE BY INDIVIDUALS 21 YRS OF AGE OR OLDER OR BY REGISTERED QUALIFYING PATIENTS ONLY. IT IS ILLEGAL TO DRIVE A MOTOR VEHICLE WHILE UNDER THE INFLUENCE OF MARIJUANA.

KEEP OUT OF REACH OF CHILDREN.

HARBORVALE SAFETY LINE CENTER
1 800 555 0147

WARNING : USE BY PREGNANT OR BREASTFEEDING WOMEN OR BY WOMEN WHO PLAN TO BECOME
PREGNANT MAY RESULT IN FETAL INJURY, PRETERM BIRTH, LOW BIRTHWEIGHT, OR DEVELOPMENTAL
PROBLEMS FOR THE CHILD.

MADE IN A MARIJUANA FACILITY

MADE & DISTRIBUTED BY MARLOWE'S TWIG COMPANY
LICENSE # BQ K 004736
(LOGO)
www.FENWILLOWS.INFO

• CMKY colors

```html
<!DOCTYPE html>
<html lang="en">
<head>
<meta charset="utf-8">
<title>Blooma Mylar Bag – Front and Back</title>
<link rel="stylesheet" href="https://fonts.googleapis.com/css2?family=Archivo+Black&family=Montserrat:wght@400;500;600&display=swap">
<style>
  :root {
    --bg: #ffffff;
    --bag-pink: #efa3bb;
    --bag-seal: #e897b1;
    --seal-line: #d98aa4;
    --white: #ffffff;
    --shadow-grey: #b9a9ae;
    --yellow: #ece45a;
    --yellow-edge: #cfc52f;
    --ink: #1d1d1d;
    --badge-green: #1f6b2e;
    --alert: #e3c62a;
  }
  * { box-sizing: border-box; margin: 0; padding: 0; }
  html, body { width: 1200px; height: 1200px; overflow: hidden; background: var(--bg); }
  .canvas { position: relative; width: 1200px; height: 1200px; }

  .bag {
    position: absolute; top: 291px; width: 507px; height: 692px;
    background: var(--bag-pink); border-radius: 10px;
    box-shadow: 0 10px 18px rgba(0,0,0,.08);
  }
  .bag--front { left: 80px; }
  .bag--back { left: 610px; }
  .bag__seal {
    position: absolute; left: 0; right: 0; top: 0; height: 92px;
    background: var(--bag-seal); border-radius: 10px 10px 0 0;
    border-bottom: 1px solid var(--seal-line);
  }
  .bag__zipper {
    position: absolute; left: 34px; right: 34px; top: 74px; height: 5px;
    border-radius: 3px; background: var(--seal-line); opacity: .6;
  }
  .bag__side {
    position: absolute; top: 92px; bottom: 20px; width: 26px;
    border-color: var(--seal-line); border-style: solid; opacity: .35;
  }
  .bag__side--left { left: 0; border-width: 0 1px 0 0; }
  .bag__side--right { right: 0; border-width: 0 0 0 1px; }
  .bag__bottom {
    position: absolute; left: 0; right: 0; bottom: 0; height: 20px;
    border-top: 1px solid var(--seal-line); opacity: .35;
  }

  /* Front */
  .front-type {
    position: absolute; left: 0; right: 0; text-align: center;
    font-family: "Archivo Black", sans-serif; line-height: 1;
  }
  .front-type--white { color: var(--white); text-shadow: 2px 3px 0 var(--shadow-grey); }
  .front-type--yellow { color: var(--yellow); -webkit-text-stroke: 1.5px var(--yellow-edge); text-shadow: 2px 3px 0 var(--shadow-grey); }
  .adult-use { top: 108px; font-size: 29px; }
  .thc { top: 147px; font-size: 72px; }
  .cereal { top: 214px; font-size: 74px; letter-spacing: -1px; }
  .frosted { top: 303px; font-size: 70px; letter-spacing: -1px; }
  .strawberry { top: 371px; font-size: 47px; letter-spacing: -1.5px; }
  .flavor { top: 419px; font-size: 48px; }
  .subtitle {
    position: absolute; left: 0; right: 0; top: 476px; text-align: center;
    font-family: "Archivo Black", sans-serif; font-size: 15px; letter-spacing: 4px;
    line-height: 18px; color: var(--white); text-shadow: 1px 1px 0 var(--shadow-grey);
  }
  .front-brand {
    position: absolute; left: 0; right: 0; top: 548px; text-align: center;
    font-family: "Montserrat", sans-serif; font-weight: 600; font-size: 38px;
    line-height: 44px; letter-spacing: 1px; color: var(--white);
  }
  .front-warning {
    position: absolute; left: 0; right: 0; top: 640px; text-align: center;
    font-family: "Archivo Black", sans-serif; font-size: 16px; letter-spacing: 2.5px;
    color: var(--white); text-shadow: 1px 1px 0 var(--shadow-grey);
  }
  .product-badge {
    position: absolute; left: 404px; top: 114px; width: 54px; height: 54px;
    border-radius: 50%; background: var(--badge-green);
  }

  /* Back label */
  .label {
    position: absolute; left: 42px; top: 149px; width: 418px; height: 492px;
    background: var(--white); border-radius: 12px;
    padding: 18px 16px 0 16px;
    font-family: "Montserrat", sans-serif; color: var(--ink);
    font-size: 11.5px; line-height: 13.3px; text-transform: uppercase;
  }
  .label h2 { font-size: 12.5px; font-weight: 600; line-height: 14px; }
  .label p { font-weight: 400; }
  .justify { text-align: justify; }
  .section { margin-bottom: 11px; }
  .ingredients-text { font-size: 13px; line-height: 13.5px; }
  .centered { text-align: center; font-weight: 500; }
  .centered--lg { font-size: 12.5px; line-height: 12px; }
  .small { font-size: 10.2px; }
  .warning-row { display: flex; align-items: center; gap: 10px; margin: 0 0 8px 0; }
  .warning-row__icon { flex: 0 0 24px; width: 24px; height: 22px; }
  .warning-row__text { font-size: 11px; line-height: 13.4px; }
  .warning-row__text--small { font-size: 9.6px; line-height: 13px; }
  .warning-row strong { font-weight: 600; }
  .label-footer {
    position: absolute; left: 16px; right: 16px; bottom: 12px; height: 50px;
    display: flex; align-items: stretch;
  }
  .label-footer__maker { flex: 0 0 214px; text-align: center; font-weight: 500; font-size: 11px; line-height: 12px; padding-top: 2px; }
  .label-footer__maker p + p { margin-top: 8px; }
  .label-footer__divider { width: 1px; background: #555; margin: 0 12px; }
  .label-footer__brand { flex: 1; min-width: 0; text-align: center; }
  .back-brand { font-weight: 600; font-size: 14px; line-height: 16px; color: var(--ink); padding-top: 2px; }
  .website { font-weight: 600; font-size: 10.5px; margin-top: 12px; white-space: nowrap; }
</style>
</head>
<body>
<main class="canvas">

  <section class="bag bag--front" aria-label="Bag front">
    <div class="bag__seal"><div class="bag__zipper"></div></div>
    <div class="bag__side bag__side--left"></div>
    <div class="bag__side bag__side--right"></div>
    <div class="bag__bottom"></div>

    <div class="product-badge" role="img" aria-label="Regulatory product symbol"></div>

    <p class="front-type front-type--white adult-use">ADULT - USE</p>
    <h1 class="front-type front-type--white thc">THC</h1>
    <p class="front-type front-type--yellow cereal">CEREAL</p>
    <p class="front-type front-type--white frosted">FROSTED</p>
    <p class="front-type front-type--white strawberry">STRAWBERRY</p>
    <p class="front-type front-type--white flavor">BLOOMA</p>
    <p class="subtitle">FROSTED STRAWBERRY<br>CEREAL ENHANCED WITH THC</p>
    <p class="front-brand">FEN WILLOWS</p>
    <p class="front-warning">KEEP OUT OF REACH OF CHILDREN</p>
  </section>

  <section class="bag bag--back" aria-label="Bag back">
    <div class="bag__seal"><div class="bag__zipper"></div></div>
    <div class="bag__side bag__side--left"></div>
    <div class="bag__side bag__side--right"></div>
    <div class="bag__bottom"></div>

    <div class="label">
      <div class="section">
        <h2>DIRECTIONS FOR USE:</h2>
        <p class="justify">THC tolerance may vary from person to person. The accepted recommendation for a new user is 10 mg THC. Reference the affixed TRALVO tag for accurate dosage information.</p>
      </div>
      <div class="section">
        <h2>INGREDIENTS</h2>
        <p class="justify ingredients-text">Rice, sugar, THC extract, coconut oil, artificial flavor &amp; color, salt, malt syrup</p>
      </div>
      <div class="section">
        <p class="centered">ALLERGEN WARNING: CONTAINS COCONUT.</p>
        <p class="centered small">MADE IN A FACULTY THAT HANDLES PEANUTS AND OTHER TREE NUTS.</p>
      </div>
      <div class="section">
        <p class="centered centered--lg">THE ACTUAL VALUE OF REPORTED CANNABINOIDS MAY<br>VARY FROM THE REPORTED VALUE BY +/-10 %</p>
        <p class="centered" style="margin-top:8px">ACTIVATION TIME: 10-60 MIN</p>
      </div>
      <div class="warning-row">
        <svg class="warning-row__icon" viewBox="0 0 24 22" aria-hidden="true">
          <polygon points="12,1.5 23,20.5 1,20.5" fill="none" stroke="var(--alert)" stroke-width="1.6" stroke-linejoin="round"/>
          <rect x="11" y="7" width="2" height="8" fill="var(--alert)"/><rect x="11" y="16.5" width="2" height="2" fill="var(--alert)"/>
        </svg>
        <p class="warning-row__text"><strong>WARNING:</strong> FOR USE BY INDIVIDUALS 21 YRS OF AGE OR OLDER OR BY REGISTERED QUALIFYING PATIENTS ONLY. IT IS ILLEGAL TO DRIVE A MOTOR VEHICLE WHILE UNDER THE INFLUENCE OF MARIJUANA.</p>
      </div>
      <div class="section">
        <p class="centered centered--lg">KEEP OUT OF REACH OF CHILDREN.<br>HARBORVALE SAFETY LINE CENTER: 1 800 555 0147</p>
      </div>
      <div class="warning-row">
        <svg class="warning-row__icon" viewBox="0 0 24 22" aria-hidden="true">
          <polygon points="12,1.5 23,20.5 1,20.5" fill="none" stroke="var(--alert)" stroke-width="1.6" stroke-linejoin="round"/>
          <rect x="11" y="7" width="2" height="8" fill="var(--alert)"/><rect x="11" y="16.5" width="2" height="2" fill="var(--alert)"/>
        </svg>
        <p class="warning-row__text warning-row__text--small"><strong>WARNING:</strong> USE BY PREGNANT OR BREASTFEEDING WOMEN OR BY WOMEN WHO PLAN TO BECOME PREGNANT MAY RESULT IN FETAL INJURY, PRETERM BIRTH, LOW BIRTHWEIGHT, OR DEVELOPMENTAL PROBLEMS FOR THE CHILD. IT IS ILLEGAL TO DRIVE A MOTOR VEHICLE WHILE UNDER THE INFLUENCE OF MARIJUANA.</p>
      </div>

      <div class="label-footer">
        <div class="label-footer__maker">
          <p>MADE IN A MARIJUANA FACILITY</p>
          <p>MADE &amp; DISTRIBUTED<br>BY MARLOWE'S TWIG COMPANY</p>
        </div>
        <div class="label-footer__divider"></div>
        <div class="label-footer__brand">
          <p class="back-brand">FEN WILLOWS</p>
          <p class="website">WWW.FENWILLOWS.INFO</p>
        </div>
      </div>
    </div>
  </section>

</main>
</body>
</html>
```